Save The Date for 2019 QRP Symposium

We have an annual meeting each June and need a Save the Date (STD) designed. It should be a two-sided postcard with room for address and stamp (according to US Mail postal standards). I have attached some examples from prior years, but we would appreciate a more modern and attractive design for this year's STD.

Target Market(s)

Our own members - nurses, nurse practitioners, PAs and physicians

Industry/Entity Type

Medical

Requirements
Must have
• Must include our logos (attached), ideally in a coordinating fashion - as was done in prior years (see examples attached) and without modifying the logos too much. Needs have the following information:
• - "Save the Date"
• - "The 12th Annual Vascular Crew Roundtable"
• - "Friday, June 7, 2019" or "6/7/19"
• - "The Halvern–Trask Building | 274 West 19th Street | NYC"
• - Please include our website (www.zq-olm.example/events), phone number (212-555-0147) and email address (ask@zq-olm.example) for people to ask questions
• - Must have space for a postage stamp and the name/address of the postcard recipient
Nice to have
• Would be nice to remain in our blue/grey/olive color palate (see attached Brand Standards guide).
Should not have
• Please do not use stock photos of medical staff. Please don't use cartoons or cartoon images (although a tasteful sketch may be considered).

```html
<!DOCTYPE html>
<html lang="en">
<head>
<meta charset="utf-8">
<title>Save The Date – 12th Annual Vascular Crew Roundtable</title>
<link rel="stylesheet" href="https://fonts.googleapis.com/css2?family=Oswald:wght@600&family=Archivo:wght@800&family=Roboto+Condensed:wght@400;700&family=Jost:wght@300&family=EB+Garamond:ital,wght@0,400;1,400&display=swap">
<style>
  :root {
    --navy: #1b3461;
    --sky: #2a8ccc;
    --ring: #86b3df;
    --mist-top: #e6f3fc;
    --mist-bottom: #cfe5f6;
    --link-blue: #2366a8;
    --rule: #1b3461;
    --white: #ffffff;
    --stage-dark: #272727;
    --stage-floor: #585858;
  }
  * { box-sizing: border-box; margin: 0; padding: 0; }
  html, body { width: 1200px; height: 528px; overflow: hidden; }
  body {
    position: relative;
    background: linear-gradient(to bottom, var(--stage-dark) 0 372px, var(--stage-floor) 372px 100%);
    font-family: "Roboto Condensed", Arial, sans-serif;
  }
  .card {
    position: absolute;
    top: 54px;
    width: 537px;
    height: 420px;
    overflow: hidden;
  }
  .card--front { left: 56px; }
  .card--back { left: 606px; background: var(--white); }
  .card__art { position: absolute; inset: 0; }

  /* Front */
  .headline {
    position: absolute; left: 212px; top: 30px;
    font-family: "Oswald", "Arial Narrow", sans-serif; font-weight: 600;
    font-size: 56px; line-height: 1; color: var(--navy); letter-spacing: 0.2px;
    white-space: nowrap;
  }
  .event-year {
    position: absolute; left: 264px; top: 122px;
    font-family: "Archivo", Arial, sans-serif; font-weight: 800;
    font-size: 30px; line-height: 1; letter-spacing: 0.5px; color: var(--white);
    white-space: nowrap;
  }
  .event-name {
    position: absolute; left: 264px; top: 153px;
    font-weight: 700; font-size: 14px; line-height: 14px; color: var(--white);
    text-transform: uppercase; letter-spacing: 0.2px; white-space: nowrap;
  }
  .event-extra {
    position: absolute; left: 264px; top: 180px;
    font-weight: 700; font-size: 14.5px; line-height: 14.5px; color: var(--white);
    white-space: nowrap;
  }
  .rule {
    position: absolute; left: 264px; height: 0;
  }
  .rule--title { top: 170px; width: 233px; border-top: 1.5px solid var(--white); }
  .rule--date { top: 245px; width: 193px; border-top: 1.5px solid var(--rule); }
  .rule--venue { top: 286px; width: 193px; border-top: 1.5px solid var(--rule); }
  .event-date {
    position: absolute; left: 264px; top: 225px;
    font-weight: 700; font-size: 17px; line-height: 18px; color: var(--sky);
    white-space: nowrap;
  }
  .event-venue {
    position: absolute; left: 264px; top: 247px;
    font-size: 16.5px; line-height: 17.6px; color: var(--link-blue);
    white-space: nowrap;
  }
  .event-contact {
    position: absolute; left: 264px; top: 288px;
    font-size: 16px; line-height: 16.8px; color: var(--link-blue);
    white-space: nowrap;
  }

  .partners {
    position: absolute; left: 0; top: 369px; width: 100%; height: 40px;
    color: var(--white); font-family: "EB Garamond", Georgia, serif;
    font-size: 8px; line-height: 9.6px;
  }
  .partner { position: absolute; top: 0; display: flex; align-items: center; gap: 10px; height: 36px; }
  .partner__seal {
    width: 36px; height: 36px; border-radius: 50%;
    border: 1px solid var(--white); flex: none;
  }
  .partner__role { font-style: italic; display: block; }
  .partner--host { left: 48px; }
  .partner--chapter { left: 188px; }
  .partner--associate { left: 352px; }

  /* Back */
  .back-copy {
    position: absolute; left: 23px; top: 64px; width: 192px;
    font-family: "Jost", Arial, sans-serif; font-weight: 300;
    font-size: 9.6px; line-height: 12.8px; color: var(--white);
  }
  .back-copy p + p { margin-top: 12.8px; }
  .return-seal {
    position: absolute; left: 223px; top: 50px;
    width: 54px; height: 54px; border-radius: 50%;
    border: 1.5px solid var(--navy);
  }
  .return-divider {
    position: absolute; left: 287px; top: 50px; width: 0; height: 54px;
    border-left: 1px solid var(--navy);
  }
  .return-address {
    position: absolute; left: 298px; top: 45px;
    font-style: normal; color: var(--navy);
  }
  .return-address__name {
    display: block; font-family: "EB Garamond", Georgia, serif; font-weight: 400;
    font-size: 21px; line-height: 22px; white-space: nowrap;
  }
  .return-address__lines {
    display: block; font-size: 9.6px; line-height: 11px; margin-top: 2px; white-space: nowrap;
  }
  .return-address__chapter { text-transform: uppercase; letter-spacing: 0.3px; }
  .stamp-box {
    position: absolute; left: 442px; top: 42px; width: 70px; height: 70px;
    border: 1.5px solid var(--navy);
  }
  .address-line {
    position: absolute; left: 284px; width: 227px; height: 0;
    border-top: 1.5px solid var(--navy);
  }
  .address-line--1 { top: 310px; }
  .address-line--2 { top: 343px; }
  .address-line--3 { top: 377px; }
</style>
</head>
<body>

<section class="card card--front" aria-label="Postcard front">
  <svg class="card__art" width="537" height="420" viewBox="0 0 537 420" aria-hidden="true">
    <defs>
      <linearGradient id="mist" x1="0" y1="0" x2="0" y2="1">
        <stop offset="0" stop-color="var(--mist-top)"/>
        <stop offset="1" stop-color="var(--mist-bottom)"/>
      </linearGradient>
    </defs>
    <rect width="537" height="420" fill="url(#mist)"/>
    <rect x="244" y="114" width="293" height="98" fill="var(--sky)"/>
    <rect x="244" y="212" width="293" height="162" fill="var(--white)"/>
    <circle cx="16" cy="210" r="254" fill="var(--ring)"/>
    <circle cx="16" cy="210" r="244" fill="var(--navy)"/>
    <path d="M70,318 C170,326 300,346 410,372 L120,372 Z" fill="var(--sky)" opacity="0.55"/>
    <path d="M0,370 C130,350 270,356 390,368 C460,376 505,368 537,356 L537,420 L0,420 Z" fill="var(--navy)"/>
  </svg>

  <svg class="card__art" width="537" height="420" viewBox="0 0 537 420" role="img" aria-label="Tasteful white line sketch of an anatomical human heart with its great vessels">
    <defs>
      <radialGradient id="sketchTone" cx="0.5" cy="0.45" r="0.6">
        <stop offset="0" stop-color="#3d5f94"/>
        <stop offset="1" stop-color="var(--navy)"/>
      </radialGradient>
    </defs>
    <rect x="30" y="44" width="182" height="300" rx="60" fill="url(#sketchTone)"/>
  </svg>

  <h1 class="headline">Save The Date</h1>

  <div class="event-year">12TH ANNUAL</div>
  <div class="event-name">Vascular Crew Roundtable</div>
  <div class="rule rule--title"></div>
  <div class="event-extra">and First-Ever ZQOLM Summer Soirée,<br>featuring Rob and the Rivertones</div>

  <div class="event-date">Friday, June 7, 2019</div>
  <div class="rule rule--date"></div>
  <div class="event-venue">The Halvern–Trask Building<br>274 West 19th Street | NYC</div>
  <div class="rule rule--venue"></div>
  <div class="event-contact">www.zq-olm.example/events<br>212-555-0147<br>Email: ask@zq-olm.example</div>

  <div class="partners">
    <div class="partner partner--host">
      <span class="partner__seal"></span>
      <span><span class="partner__role">Presented by</span>The Zephyr Quill<br>Society, Inc.</span>
    </div>
    <div class="partner partner--chapter">
      <span class="partner__seal"></span>
      <span><span class="partner__role">of the</span>New York State Chapter,<br>Olmsted League of Medicine</span>
    </div>
    <div class="partner partner--associate">
      <span class="partner__seal"></span>
      <span><span class="partner__role">In association with</span>Brightwater Heart Center</span>
    </div>
  </div>
</section>

<section class="card card--back" aria-label="Postcard back">
  <svg class="card__art" width="537" height="420" viewBox="0 0 537 420" aria-hidden="true">
    <circle cx="-180" cy="210" r="434" fill="var(--ring)"/>
    <circle cx="-180" cy="210" r="422" fill="var(--navy)"/>
  </svg>

  <div class="back-copy">
    <p>Join us for great events at The<br>Halvern–Trask Building, 274 West<br>19th Street | NYC, New York, this June!</p>
    <p>Now in its tenth year, the Annual Vascular Crew (QRP) Roundtable is a unique all-day academic event designed to enhance current knowledge about the etiology, prevention, intervention and management of cardiovascular disease.</p>
    <p>In the evening, the New York State Chapter of the OLM will host its first-ever Summer Soirée, featuring the band Rob &amp; the Rivertones playing us off into the night.</p>
    <p>A courtesy block of rooms has already been secured at The Larkspur Inn for these two events. To reserve a room at the discounted rate, please call (800) 555-0193 and be sure to mention “The Zephyr Quill Society.”</p>
  </div>

  <span class="return-seal"></span>
  <span class="return-divider"></span>
  <address class="return-address">
    <span class="return-address__name">Olmsted League</span>
    <span class="return-address__lines">
      <span class="return-address__chapter">Chapter</span><br>
      418 Ninth Avenue, Ste. 1207<br>
      New York, NY 10099
    </span>
  </address>

  <div class="stamp-box"></div>
  <div class="address-line address-line--1"></div>
  <div class="address-line address-line--2"></div>
  <div class="address-line address-line--3"></div>
</section>

</body>
</html>
```